Eye-catching Card for new church

I would like a card the size of a business card ... that can be used to announce the start of our new church. I would like it to have our logo on the card, my name, and the statement "Coming Soon ... 1.10.2016". I also would like to list our website address and Facebook page and my Twitter account.

Target Market(s)

prospective people looking for a church

Industry/Entity Type

Church

Requirements
Must have
• a focus on Coming Soon ... 1.10.2016
• Brightfield Church logo
Should not have
• church buildings or writings on the cross

```html
<!DOCTYPE html>
<html lang="en">
<head>
<meta charset="utf-8">
<title>Brightfield Church – Business Card</title>
<link rel="stylesheet" href="https://fonts.googleapis.com/css2?family=Exo+2:wght@400;500;600&display=swap">
<style>
  :root {
    --page-bg: #e9eaec;
    --card-white: #ffffff;
    --card-edge: #f1f2f3;
    --blue-light: #4fb3f0;
    --blue-mid: #2f86dc;
    --blue-deep: #1f4fb8;
    --stripe-grey: #6b6e72;
    --text-white: #ffffff;
    --logo-ink: #3a3c40;
    --logo-accent: #2a72d6;
    --muted-ink: #6b6e72;
  }
  * { box-sizing: border-box; margin: 0; padding: 0; }
  html, body {
    width: 1200px; height: 900px; overflow: hidden;
    background: var(--page-bg);
    font-family: "Exo 2", sans-serif;
  }
  .canvas {
    width: 1200px; height: 900px;
    display: flex; align-items: center; justify-content: center; gap: 44px;
  }
  .card {
    position: relative;
    width: 540px; height: 310px;
    border-radius: 30px;
    overflow: hidden;
    background: linear-gradient(135deg, var(--card-white) 55%, var(--card-edge));
    box-shadow: 0 10px 28px rgba(0,0,0,0.14);
  }
  .card-front__panel { position: absolute; inset: 0; }
  .contact {
    position: absolute; left: 26px; top: 24px; width: 205px;
    color: var(--text-white);
  }
  .contact__name {
    font-size: 15px; font-weight: 500; letter-spacing: 0.5px; text-transform: uppercase;
  }
  .contact__role { font-size: 11px; margin-top: 2px; }
  .contact__address { font-size: 11px; line-height: 1.45; margin-top: 16px; }
  .contact__list { list-style: none; margin-top: 10px; }
  .contact__item {
    display: flex; align-items: center; gap: 8px;
    font-size: 10.5px; line-height: 1.85; letter-spacing: 0.3px;
    white-space: nowrap;
  }
  .contact__icon { width: 10px; height: 10px; flex: none; fill: var(--text-white); }
  .brand {
    display: flex; align-items: center; gap: 10px;
    font-weight: 500;
    color: var(--logo-ink);
    letter-spacing: 3px; text-transform: uppercase;
    white-space: nowrap;
  }
  .brand__mark { width: 14px; height: 14px; background: var(--logo-accent); flex: none; }
  .card-front .brand {
    position: absolute; left: 262px; top: 144px; font-size: 17px; letter-spacing: 2.5px;
  }
  .announce {
    position: absolute; inset: 0;
    display: flex; flex-direction: column; align-items: center; justify-content: center;
    gap: 18px;
  }
  .card-back .brand { font-size: 24px; }
  .announce__rule { width: 220px; height: 2px; background: var(--stripe-grey); opacity: 0.5; }
  .announce__headline {
    font-size: 32px; font-weight: 600; color: var(--logo-accent);
    letter-spacing: 1px; white-space: nowrap; text-align: center;
  }
  .announce__date { display: block; font-size: 20px; font-weight: 500; color: var(--logo-ink); letter-spacing: 4px; margin-top: 4px; }
</style>
</head>
<body>
<main class="canvas">
  <section class="card card-front" aria-label="Business card front">
    <svg class="card-front__panel" viewBox="0 0 540 310" preserveAspectRatio="none" aria-hidden="true">
      <defs>
        <radialGradient id="panelBlue" cx="0.35" cy="0.65" r="0.9">
          <stop offset="0" stop-color="#4fb3f0"/>
          <stop offset="0.55" stop-color="#2f86dc"/>
          <stop offset="1" stop-color="#1f4fb8"/>
        </radialGradient>
      </defs>
      <path d="M0 0 H246 Q222 150 238 310 H0 Z" fill="#6b6e72"/>
      <path d="M0 0 H236 Q212 150 228 310 H0 Z" fill="url(#panelBlue)"/>
    </svg>
    <div class="contact">
      <p class="contact__name">Daniel Mercer</p>
      <p class="contact__role">Managing Director</p>
      <p class="contact__address">41 Harbor Lane, Suite 2<br>Cedar Hill, OR</p>
      <ul class="contact__list">
        <li class="contact__item">
          <svg class="contact__icon" viewBox="0 0 10 10"><path d="M2 0.5 L3.6 2.6 L2.6 3.6 Q3.8 5.9 6.4 7.4 L7.4 6.4 L9.5 8 L8.3 9.5 Q3.5 9 0.5 1.7 Z"/></svg>
          012 555 0142
        </li>
        <li class="contact__item">
          <svg class="contact__icon" viewBox="0 0 10 10"><rect x="2.5" y="0.5" width="5" height="9" rx="1"/></svg>
          012 555 0143
        </li>
        <li class="contact__item">
          <svg class="contact__icon" viewBox="0 0 10 10"><path d="M0.5 2 H9.5 V8.5 H0.5 Z M1 2.4 L5 5.6 L9 2.4" fill="none" stroke="#fff" stroke-width="1"/></svg>
          hello@brightfieldchurch.org
        </li>
        <li class="contact__item">
          <svg class="contact__icon" viewBox="0 0 10 10"><circle cx="5" cy="5" r="4.3" fill="none" stroke="#fff" stroke-width="1"/><path d="M0.7 5 H9.3 M5 0.7 Q2.4 5 5 9.3 M5 0.7 Q7.6 5 5 9.3" fill="none" stroke="#fff" stroke-width="0.8"/></svg>
          www.brightfieldchurch.org
        </li>
        <li class="contact__item">
          <svg class="contact__icon" viewBox="0 0 10 10"><rect x="0.5" y="0.5" width="9" height="9" rx="1.5"/></svg>
          Facebook: /brightfieldchurch
        </li>
        <li class="contact__item">
          <svg class="contact__icon" viewBox="0 0 10 10"><circle cx="5" cy="5" r="4.5"/></svg>
          Twitter: @danielmercer
        </li>
      </ul>
    </div>
    <div class="brand"><span class="brand__mark"></span>Brightfield Church</div>
  </section>

  <section class="card card-back" aria-label="Business card back">
    <div class="announce">
      <div class="brand"><span class="brand__mark"></span>Brightfield Church</div>
      <span class="announce__rule"></span>
      <p class="announce__headline">Coming Soon ...<span class="announce__date">1.10.2016</span></p>
    </div>
  </section>
</main>
</body>
</html>
```